Online tuition webpage design needed

Hi,
We are starting up an online tuition website for non- English speakers wishing to take an QRAVE test.

The webpage must include a place for people to enroll online in the course.
The home page must have:
• room for a logo (coming shortly, blue in colour)
• different packages of online tuition and coinvy
• tool bar showing different pages
• perhaps a video, small pictures

This is my site currently:-

www.lernmarowebtutor.example

as you can see, I am not very sure how to create a website … The large logo is what I would like to use, but I project has not been finalized yet. Please note, I don’t like the logo being that large!

Sites that are similar to what I am doing and like the design of are:

http://www.quorvapath.example.au/fees

https://www.brantiq9.example/index.php

http://www.tutorhalvekmorris.example.uk/index.html

http://www.vorplaneexam.example/

One thing I need is a place for student s to enroll, and if possible, I would like to use plovix to create exercises for students.
Currently, my site is using sitequill. My preference is to use plovix for online activities. I am not sure if I can use both.
Thanks in advance

Target Market(s)

people wising to take an QRAVE test (English proficiency test)

Industry/Entity Type

Online

Colors
3276b5
0292cd

Requirements
Must have
• a place for enrollment and admin login for students
plovix
video
talvo, gatherly, chirrup logos
Nice to have
• a booking calender
Should not have
• too much clutter. must be clean and professional looking

```html
<!DOCTYPE html>
<html lang="en">
<head>
<meta charset="utf-8">
<title>QRAVE Online Tuition</title>
<link href="https://fonts.googleapis.com/css2?family=Arimo:wght@400;700&family=Montserrat:wght@400;500&display=swap" rel="stylesheet">
<style>
:root{
  --blue:#0292cd;
  --blue-deep:#3276b5;
  --blue-text:#1a8fcf;
  --nav-top:#2aa8de;
  --nav-bottom:#0a87c1;
  --panel:#e8e8e7;
  --grey-text:#8a8a8a;
  --line:#c9c9c9;
  --white:#ffffff;
  --dark:#1f1f1f;
  --chirrup:#3ca9e0;
  --gatherly:#3b5ea8;
  --talvo:#1a8fd6;
  --feed:#f08a1c;
  --today:#e0502f;
}
*{box-sizing:border-box;margin:0;padding:0}
html,body{width:1200px;height:2446px;overflow:hidden;background:var(--white)}
body{position:relative;font-family:"Arimo",Arial,sans-serif;color:var(--dark)}
.abs{position:absolute}

/* header */
.brand{left:73px;top:42px}
.brand-name{font-size:52px;font-weight:400;color:var(--blue-deep);letter-spacing:1px;line-height:1;margin-left:44px}
.brand-tag{font-size:18px;color:var(--blue-deep);margin-left:86px;margin-top:2px}
.social{display:flex;gap:9px}
.social span{width:28px;height:28px;border-radius:50%;display:block}
.s-chirrup{background:var(--chirrup)}
.s-gatherly{background:var(--gatherly)}
.s-talvo{background:var(--talvo)}
.s-feed{background:var(--feed)}
.social-top{left:939px;top:59px}
.search{left:913px;top:104px;width:179px;height:40px;border:1.5px solid #9fcfe8;border-radius:6px;font-size:12px;color:var(--blue-text);padding:12px 0 0 17px;letter-spacing:.5px}
.search svg{position:absolute;right:12px;top:8px}

/* nav */
.nav{left:0;top:161px;width:1200px;height:48px;background:linear-gradient(var(--nav-top),var(--nav-bottom))}
.nav a{position:absolute;top:12px;font-size:20px;color:var(--white);text-decoration:none}

/* hero */
.hero{left:0;top:209px;width:1200px;height:544px;background:linear-gradient(110deg,#3d4147 0%,#6b6f6a 35%,#8e9587 55%,#4c5d3e 80%,#2b2f2c 100%)}
.hero-band{left:0;top:365px;width:1200px;height:132px;background:rgba(70,70,70,.72)}
.hero-title{left:0;top:392px;width:1200px;text-align:center;color:var(--white);font-size:40px;line-height:38px;letter-spacing:.5px}
.cta{left:437px;top:548px;width:323px;height:62px;border-radius:31px;background:linear-gradient(#1ea3dc,#0a7fb8);color:var(--white);font-size:23px;text-align:center;line-height:62px;box-shadow:0 3px 6px rgba(0,0,0,.35)}

/* features */
.feature-photo{border-radius:50%}
.ring-white{border:7px solid var(--white);box-shadow:0 0 3px rgba(0,0,0,.25)}
.ring-blue{border:6px solid var(--blue)}
.caption{font-size:16px;color:var(--blue-text);text-align:center;line-height:18px;width:260px}

/* how it works */
.how{left:0;top:1268px;width:1200px;height:605px;background:linear-gradient(100deg,#0b5f8c,#0f7db5 45%,#0a6fa6 70%,#137fb6)}
.how-title{left:0;top:1307px;width:1200px;text-align:center;font-size:32px;color:var(--white)}
.how-text{left:236px;top:1368px;width:676px;text-align:center;font-size:16px;line-height:24px;color:var(--white)}
.video{left:323px;top:1462px;width:551px;height:334px;background:linear-gradient(120deg,#e9ecef,#c7d3dd 40%,#7d9dc4 70%,#d9dde0);overflow:hidden}
.video-bar{left:0;bottom:0;width:551px;height:30px;background:#202020}
.video-progress{left:0;bottom:30px;width:551px;height:6px;background:#555}
.video-progress i{display:block;width:40px;height:6px;background:#d52b1e}
.video-time{left:78px;bottom:8px;font-size:11px;color:#ddd}
.video-play{left:239px;top:129px;width:73px;height:52px;border-radius:10px;background:rgba(25,25,25,.9)}

/* panels */
.panel{top:1925px;width:442px;height:364px;background:var(--panel);border-radius:26px;box-shadow:0 5px 4px rgba(0,0,0,.18)}
.panel-title{position:absolute;left:38px;top:26px;font-size:25px;color:var(--blue-text)}
.panel-rule{position:absolute;left:38px;top:65px;width:366px;height:1px;background:var(--line)}
.testimonial{position:absolute;left:44px;width:370px}
.avatar{position:absolute;left:0;top:0;width:90px;height:90px;border-radius:50%;border:5px solid var(--blue);background:linear-gradient(#d9d3cf,#b7a49a)}
.quote{position:absolute;left:108px;top:-1px;width:215px;font-size:14px;line-height:19.5px;color:var(--grey-text);text-align:justify}
.author{display:block;color:var(--blue-text);margin-top:2px}

.calendar{position:absolute;left:83px;top:82px;width:274px;border:1px solid #d0d0d0;background:var(--white);font-family:"Montserrat",Arial,sans-serif;box-shadow:0 3px 0 #c4c4c4}
.cal-head{height:34px;background:#ececec;display:flex;justify-content:space-between;align-items:center;padding:0 10px;font-size:15px;letter-spacing:1px;color:#444}
.cal-grid{display:grid;grid-template-columns:repeat(7,1fr)}
.cal-grid span{height:34px;border-right:1px solid #e2e2e2;border-top:1px solid #e2e2e2;text-align:center;line-height:34px;font-size:13px;color:#333}
.cal-grid span:nth-child(7n){border-right:0}
.cal-grid .muted{color:#c2c2c2}
.cal-grid .today{color:var(--today);border:1px solid var(--today)}

/* footer */
.social-foot{left:921px;top:2359px}
.footer{left:0;top:2408px;width:1200px;height:38px;background:var(--blue)}
.footer-links{left:148px;top:12px;font-size:12px;color:var(--white)}
.footer-links b{font-weight:400;margin:0 9px}
.copyright{right:130px;top:12px;font-size:12px;color:var(--white)}
</style>
</head>
<body>

<header>
  <div class="abs brand">
    <div class="brand-name">QRAVE</div>
    <div class="brand-tag">Online Tuition</div>
  </div>
  <div class="abs social social-top">
    <span class="s-chirrup"></span><span class="s-gatherly"></span><span class="s-talvo"></span><span class="s-feed"></span>
  </div>
  <div class="abs search">SEARCH
    <svg width="22" height="22" viewBox="0 0 22 22"><circle cx="8.5" cy="8.5" r="6" fill="none" stroke="#1a8fcf" stroke-width="2.5"/><line x1="13" y1="13" x2="20" y2="20" stroke="#1a8fcf" stroke-width="3" stroke-linecap="round"/></svg>
  </div>
</header>

<nav class="abs nav">
  <a style="left:73px">Home</a>
  <a style="left:171px">Tutorial Packages</a>
  <a style="left:367px">Weekly Tips &amp; Comments</a>
  <a style="left:631px">Reading</a>
  <a style="left:748px">Speaking</a>
  <a style="left:874px">Listening</a>
  <a style="left:996px">Writing</a>
</nav>

<section>
  <div class="abs hero" role="img" aria-label="Photo of a laptop and headphones on a wooden desk by a window"></div>
  <div class="abs hero-band"></div>
  <h1 class="abs hero-title" style="font-weight:400">WE PUT YOU FIRST. WE LISTEN TO YOU<br>AND HELP YOU FIND WHAT YOU NEED.</h1>
  <div class="abs cta">LEARN MORE</div>
</section>

<section>
  <div class="abs feature-photo ring-white" style="left:218px;top:655px;width:212px;height:212px;background:linear-gradient(135deg,#9aa1a8,#2c2f33)" role="img" aria-label="Photo of hands typing on a keyboard"></div>
  <div class="abs feature-photo ring-white" style="left:499px;top:655px;width:212px;height:212px;background:linear-gradient(160deg,#e4e7ea,#5b6168)" role="img" aria-label="Photo of a tutor with a headset at a laptop"></div>
  <div class="abs feature-photo ring-white" style="left:792px;top:655px;width:212px;height:212px;background:linear-gradient(180deg,#8a6a4f,#c9a46c 60%,#9c7640)" role="img" aria-label="Photo of a student on a video call"></div>
  <div class="abs caption" style="left:194px;top:894px">Lessons in reading, writing,<br>listening and speaking</div>
  <div class="abs caption" style="left:475px;top:894px">Professional teacher feedback<br>and tips.</div>
  <div class="abs caption" style="left:775px;top:894px">Talvo and practice with native<br>speakers.</div>

  <div class="abs feature-photo ring-blue" style="left:372px;top:959px;width:214px;height:214px;background:linear-gradient(170deg,#f2f2f2,#8d9199)" role="img" aria-label="Photo of a smiling student giving a thumbs up"></div>
  <div class="abs feature-photo ring-blue" style="left:666px;top:959px;width:214px;height:214px;background:linear-gradient(170deg,#f4f4f4,#a9c7dc)" role="img" aria-label="Photo of a friendly teacher in a classroom"></div>
  <div class="abs caption" style="left:349px;top:1198px">Quick Turnaround.</div>
  <div class="abs caption" style="left:649px;top:1198px">Friendly and Approachable<br>teachers.</div>
</section>

<section>
  <div class="abs how" role="img" aria-label="Blue-tinted photo of students studying together at a laptop"></div>
  <h2 class="abs how-title" style="font-weight:400">HOW IT WORKS</h2>
  <p class="abs how-text">Lorem ipsum dolor sit amet, consectetur adipiscing elit. Curabitur non tincidunt nisl. In placerat mi sed arcu pharetra rhoncus. Suspendisse non sodales tortor, vel porttitor nisl.</p>
  <div class="abs video" role="img" aria-label="Video still of a student on the phone at a laptop">
    <div class="abs video-play"><svg width="73" height="52" viewBox="0 0 73 52"><path d="M29 16 L47 26 L29 36 Z" fill="#fff"/></svg></div>
    <div class="abs video-progress"><i></i></div>
    <div class="abs video-bar">
      <svg class="abs" style="left:14px;top:8px" width="14" height="14" viewBox="0 0 14 14"><path d="M2 1 L12 7 L2 13 Z" fill="#ccc"/></svg>
    </div>
    <div class="abs video-time">0:15 / 0:39</div>
  </div>
</section>

<section>
  <div class="abs panel" style="left:140px">
    <h3 class="panel-title" style="font-weight:400">CLIENT TESTIMONIALS</h3>
    <div class="panel-rule"></div>
    <div class="testimonial" style="top:95px">
      <div class="avatar" role="img" aria-label="Client portrait"></div>
      <p class="quote">Lorem ipsum dolor sit amet, consectetur adipiscing elit. Curabitur non tincidunt nisl. In placerat mi.<span class="author">Rob Doe</span></p>
    </div>
    <div class="testimonial" style="top:219px">
      <div class="avatar" role="img" aria-label="Client portrait"></div>
      <p class="quote">Lorem ipsum dolor sit amet, consectetur adipiscing elit. Curabitur non tincidunt nisl. In placerat mi.<span class="author">Rob Doe</span></p>
    </div>
  </div>

  <div class="abs panel" style="left:641px">
    <h3 class="panel-title" style="font-weight:400">BOOKING CALENDAR</h3>
    <div class="panel-rule"></div>
    <div class="calendar">
      <div class="cal-head"><span>&lsaquo;</span><span>NOVEMBER</span><span>&rsaquo;</span></div>
      <div class="cal-grid">
        <span class="muted">29</span><span class="muted">30</span><span class="muted">31</span><span>1</span><span>2</span><span>3</span><span>4</span>
        <span>5</span><span>6</span><span>7</span><span>8</span><span>9</span><span>10</span><span>11</span>
        <span>12</span><span>13</span><span>14</span><span>15</span><span>16</span><span>17</span><span>18</span>
        <span>19</span><span>20</span><span>21</span><span>22</span><span class="today">23</span><span>24</span><span>25</span>
        <span>26</span><span>27</span><span>28</span><span>29</span><span>30</span><span class="muted">1</span><span class="muted">2</span>
      </div>
    </div>
  </div>
</section>

<footer>
  <div class="abs social social-foot">
    <span class="s-chirrup"></span><span class="s-gatherly"></span><span class="s-talvo"></span><span class="s-feed"></span>
  </div>
  <div class="abs footer">
    <div class="abs footer-links">Sitemap<b>|</b>Contact us<b>|</b>Terms &amp; Usage</div>
    <div class="abs copyright">Copyright © 2013. QRAVE Online Tuition All Rights Reserved.</div>
  </div>
</footer>

</body>
</html>
```